infographic

Infographic to be posted on chatterloop, website and shared by email very simply illustrating the below:

Meridian has doubled access to paid parental leave:
• Only about 50 per cent of working women had access to paid maternity leave before the Government introduced its scheme on 1 January 2011.
• Today 95 per cent of working women have access to paid parental leave (18 weeks at minimum wage)

Target Market(s)

women aged 30-45 with kids

Industry/Entity Type

Government

Requirements
Must have
• please use red for the 95% and blue for the 50% (red is meridian's colour)

```html
<!DOCTYPE html>
<html lang="en">
<head>
<meta charset="utf-8">
<title>Meridian has doubled access to paid parental leave</title>
<link rel="stylesheet" href="https://fonts.googleapis.com/css2?family=Alfa+Slab+One&family=Bebas+Neue&family=Advent+Pro:wght@300;400&family=Oswald:wght@500;700&family=Share+Tech+Mono&display=swap">
<style>
  :root{
    --paper:#dcdcdc;
    --paper-light:#ececec;
    --paper-dark:#c4c6c9;
    --bar-dark:#58595b;
    --bar-light:#f4f4f4;
    --red:#ed1c24;
    --red-soft:#f07a80;
    --brown:#5b4a40;
    --ink:#333333;
    --grey-text:#6d6e70;
    --blue:#1a75bb;
    --blue-half:#3d8fd0;
    --blue-deep:#2a5caa;
    --white:#ffffff;
  }
  html,body{margin:0;padding:0;overflow:hidden;}
  body{width:900px;height:1200px;}
  .infographic{
    position:relative;width:900px;height:1200px;overflow:hidden;
    background:radial-gradient(ellipse at 50% 45%,var(--paper-light) 0%,var(--paper) 55%,var(--paper-dark) 100%);
  }
  .abs{position:absolute;margin:0;}
  .bar{position:absolute;height:12px;background:var(--bar-dark);}
  .bar--light{height:6px;background:var(--bar-light);}
  .brand-name{
    left:400px;top:78px;width:100px;text-align:center;
    font-family:'Bebas Neue',sans-serif;font-size:26px;color:var(--red);letter-spacing:1px;
  }
  .brand-dot{position:absolute;left:441px;top:62px;width:18px;height:18px;border-radius:50%;background:var(--red);}
  .headline{
    left:55px;top:148px;width:790px;text-align:center;
    font-family:'Bebas Neue',sans-serif;font-weight:400;color:var(--red);
  }
  .headline span{display:block;white-space:nowrap;}
  .headline .l1{font-size:70px;line-height:62px;letter-spacing:1px;}
  .headline .l2{font-size:80px;line-height:70px;letter-spacing:0;}
  .before-lead{
    left:62px;top:360px;
    font-family:'Alfa Slab One',serif;font-size:84px;line-height:86px;font-style:italic;
    color:var(--paper-light);
    -webkit-text-stroke:2px var(--ink);
    text-shadow:5px 5px 0 var(--ink);
    transform:skewX(-10deg);
  }
  .before-tail{
    left:585px;top:374px;width:255px;text-align:right;white-space:nowrap;
    font-family:'Alfa Slab One',serif;font-size:31px;line-height:44px;
    color:var(--paper-light);-webkit-text-stroke:1.5px var(--ink);
    text-shadow:3px 3px 0 var(--ink);transform:skewX(-10deg);
  }
  .pie{position:absolute;}
  .pie-label{position:absolute;text-align:center;color:var(--white);}
  .pie-label--before{
    left:352px;top:403px;width:110px;
    font-family:'Alfa Slab One',serif;font-size:14px;line-height:18px;font-style:italic;
  }
  .pie-label--before b{font-family:'Bebas Neue',sans-serif;font-weight:400;font-size:36px;line-height:36px;font-style:normal;}
  .divider-red{left:55px;top:591px;width:795px;height:1px;background:var(--red);}
  .before-the{
    left:74px;top:604px;white-space:nowrap;
    font-family:'Advent Pro',sans-serif;font-weight:300;font-size:80px;letter-spacing:10px;line-height:80px;
    color:transparent;-webkit-text-stroke:1.5px var(--brown);
    transform:scaleY(1.2);transform-origin:top left;
  }
  .government{
    left:72px;top:672px;white-space:nowrap;
    font-family:'Advent Pro',sans-serif;font-weight:400;font-size:86px;letter-spacing:5px;line-height:86px;
    color:var(--brown);
    transform:scaleY(1.4);transform-origin:top left;
  }
  .scheme-date{
    left:75px;top:790px;white-space:nowrap;
    font-family:'Share Tech Mono',monospace;font-size:23px;letter-spacing:8px;color:var(--grey-text);
    text-transform:uppercase;
  }
  .today{
    left:75px;top:890px;width:248px;text-align:center;white-space:nowrap;
    font-family:'Bebas Neue',sans-serif;font-weight:400;font-size:116px;line-height:116px;color:var(--red);
    transform:scaleY(1.3);transform-origin:top center;
  }
  .bar--accent{background:var(--red);height:8px;}
  .pie-label--today{
    left:450px;top:890px;width:130px;
    font-family:'Oswald',sans-serif;font-weight:500;font-size:22px;line-height:22px;
  }
  .pie-label--today b{display:block;font-size:52px;line-height:58px;font-weight:500;}
  .today-tail{
    left:598px;top:878px;width:248px;
    font-family:'Bebas Neue',sans-serif;color:var(--red);text-align:center;white-space:nowrap;
    transform:scaleY(1.3);transform-origin:top center;
  }
  .today-tail .t1,.today-tail .t2{display:block;font-size:44px;line-height:40px;}
  .today-tail .t3{display:block;font-family:'Oswald',sans-serif;font-weight:700;font-size:38px;line-height:44px;letter-spacing:12px;}
  .today-tail .t4{display:block;font-family:'Oswald',sans-serif;font-weight:500;font-size:16px;line-height:20px;}
</style>
</head>
<body>
<main class="infographic">

  <div class="brand-dot"></div>
  <p class="abs brand-name">Meridian</p>

  <div class="bar" style="left:55px;top:118px;width:343px;"></div>
  <div class="bar" style="left:508px;top:118px;width:330px;"></div>
  <div class="bar bar--light" style="left:55px;top:136px;width:783px;"></div>

  <h1 class="abs headline">
    <span class="l1">MERIDIAN HAS DOUBLED ACCESS</span>
    <span class="l2">TO PAID PARENTAL LEAVE:</span>
  </h1>

  <div class="bar bar--light" style="left:55px;top:302px;width:783px;"></div>
  <div class="bar" style="left:55px;top:322px;width:783px;"></div>

  <p class="abs before-lead">Only<br>about</p>

  <svg class="pie" style="left:350px;top:337px" width="226" height="226" viewBox="0 0 226 226" role="img" aria-label="Pie chart: 50 per cent">
    <circle cx="113" cy="113" r="113" fill="var(--blue-half)"/>
    <path d="M113 0 A113 113 0 0 0 113 226 Z" fill="var(--blue)"/>
    <line x1="113" y1="0" x2="113" y2="226" stroke="var(--paper-light)" stroke-width="3"/>
  </svg>
  <p class="pie-label pie-label--before"><b>50%</b> of<br>working<br>women</p>

  <p class="abs before-tail">had access<br>to paid<br>maternity<br>leave before</p>

  <div class="abs divider-red"></div>

  <p class="abs before-the">BEFORE THE</p>
  <p class="abs government">GOVERNMENT</p>

  <svg class="abs" style="left:590px;top:600px" width="245" height="182" viewBox="0 0 245 182" aria-hidden="true">
    <polygon points="122,0 10,36 234,36" fill="var(--brown)"/>
    <rect x="10" y="40" width="224" height="12" fill="var(--brown)"/>
    <rect x="22" y="62" width="30" height="82" fill="var(--brown)"/>
    <rect x="78" y="62" width="30" height="82" fill="var(--brown)"/>
    <rect x="136" y="62" width="30" height="82" fill="var(--brown)"/>
    <rect x="192" y="62" width="30" height="82" fill="var(--brown)"/>
    <rect x="12" y="148" width="220" height="10" fill="var(--brown)"/>
    <rect x="4" y="160" width="236" height="10" fill="var(--brown)"/>
    <rect x="0" y="172" width="245" height="10" fill="var(--brown)"/>
  </svg>

  <p class="abs scheme-date">Introduced its scheme on 1 January 2011</p>

  <svg class="abs" style="left:75px;top:822px" width="775" height="20" viewBox="0 0 775 20" aria-hidden="true">
    <line x1="0" y1="10" x2="758" y2="10" stroke="var(--brown)" stroke-width="2"/>
    <polygon points="756,2 775,10 756,18" fill="var(--brown)"/>
  </svg>

  <div class="bar bar--accent" style="left:75px;top:868px;width:248px;"></div>
  <div class="bar bar--accent" style="left:75px;top:883px;width:248px;height:4px;"></div>
  <p class="abs today">TODAY</p>
  <div class="bar bar--accent" style="left:75px;top:1028px;width:248px;height:4px;"></div>
  <div class="bar bar--accent" style="left:75px;top:1040px;width:248px;"></div>

  <svg class="pie" style="left:330px;top:855px" width="250" height="250" viewBox="0 0 250 250" role="img" aria-label="Pie chart: 95 per cent">
    <circle cx="125" cy="125" r="125" fill="var(--red)"/>
    <path d="M125 125 L125 0 A125 125 0 0 1 163.6 6.1 Z" fill="var(--red-soft)" transform="rotate(-18 125 125)"/>
  </svg>
  <p class="pie-label pie-label--today"><b>95%</b>OF WORKING<br>WOMEN</p>

  <p class="abs today-tail">
    <span class="t1">HAVE ACCESS TO</span>
    <span class="t2">PAID PARENTAL</span>
    <span class="t3">LEAVE</span>
    <span class="t4">(18 WEEKS AT MINIMUM WAGE)</span>
  </p>

</main>
</body>
</html>
```